Falcrest security business card

Looking for a business card for my security company

Target Market(s)

Security

Industry/Entity Type

Security

Contact Information for Business Card

Name - Gil Marston. Title - General manager - direct 314 862.4490 website www. falcrestsecurityservices.example email - gil@ falcrestsecurityservices.example

Requirements
Must have
• Logo attached

```html
<!DOCTYPE html>
<html lang="en">
<head>
<meta charset="utf-8">
<title>Falcrest Security Services – Business Card</title>
<link rel="stylesheet" href="https://fonts.googleapis.com/css2?family=Montserrat:wght@300;400;600;700&display=swap">
<style>
  :root {
    --stage: #e4e4e4;
    --ink: #0d0d0d;
    --paper-white: #ffffff;
    --gold-light: #ecdd98;
    --gold-mid: #dcb352;
    --gold-deep: #b0722a;
    --gold-text: #e2b452;
    --web-text: #3a2a14;
  }
  * { margin: 0; padding: 0; box-sizing: border-box; }
  html, body {
    width: 1200px; height: 800px; overflow: hidden;
    background: var(--stage);
    font-family: "Montserrat", sans-serif;
  }
  .stage { position: relative; width: 1200px; height: 800px; }
  .card {
    position: absolute; top: 257px;
    width: 500px; height: 286px;
    overflow: hidden;
    box-shadow: 0 10px 28px rgba(0,0,0,0.18);
  }
  .card--front { left: 60px; }
  .card--back { left: 640px; }
  .card__bands { position: absolute; inset: 0; width: 100%; height: 100%; }

  .wordmark {
    position: absolute;
    font-weight: 700; font-size: 40px;
    letter-spacing: 1.5px; text-transform: uppercase;
    line-height: 1; white-space: nowrap;
    display: flex; align-items: center; gap: 12px;
  }
  .wordmark__dot { width: 12px; height: 12px; border-radius: 50%; flex: none; }
  .card--front .wordmark { left: 114px; top: 108px; color: var(--paper-white); }
  .card--front .wordmark__dot { background: var(--paper-white); }
  .card--back .wordmark { left: 104px; top: 112px; color: var(--gold-text); }
  .card--back .wordmark__dot { background: var(--gold-text); }

  .person {
    position: absolute; left: 34px; top: 204px;
    color: var(--paper-white);
  }
  .person__name { font-size: 23px; font-weight: 300; line-height: 1.1; }
  .person__name strong { font-weight: 600; }
  .person__title { font-size: 13px; font-weight: 300; margin-top: 3px; }

  .divider {
    position: absolute; left: 196px; top: 200px;
    width: 1px; height: 50px; background: var(--paper-white);
  }
  .contacts {
    position: absolute; left: 208px; top: 204px;
    list-style: none; color: var(--paper-white);
    font-size: 11.5px; font-weight: 300;
  }
  .contacts li { display: flex; align-items: center; gap: 6px; height: 21px; }
  .contacts svg { width: 12px; height: 12px; flex: none; }

  .website {
    position: absolute; left: 0; right: 0; top: 240px;
    text-align: center;
    font-size: 13px; letter-spacing: 3px; font-weight: 400;
    color: var(--web-text);
  }
</style>
</head>
<body>
<main class="stage">

  <section class="card card--front" aria-label="Business card front">
    <svg class="card__bands" viewBox="0 0 500 286" aria-hidden="true">
      <defs>
        <linearGradient id="goldFront" x1="0" y1="0" x2="1" y2="1">
          <stop offset="0" stop-color="var(--gold-light)"/>
          <stop offset="0.5" stop-color="var(--gold-mid)"/>
          <stop offset="1" stop-color="var(--gold-deep)"/>
        </linearGradient>
      </defs>
      <rect width="500" height="286" fill="url(#goldFront)"/>
      <polygon fill="var(--ink)"
        points="0,176 96,176 96,84 414,84 414,140 500,140 500,286 0,286"/>
    </svg>
    <div class="wordmark"><span class="wordmark__dot"></span>Falcrest</div>
    <div class="person">
      <p class="person__name"><strong>Gil</strong> Marston</p>
      <p class="person__title">General manager</p>
    </div>
    <span class="divider"></span>
    <ul class="contacts">
      <li>
        <svg viewBox="0 0 12 12" aria-hidden="true"><circle cx="6" cy="6" r="6" fill="#fff"/><path d="M4 3.2l1 1.6-.6.6c.4.9 1 1.5 1.9 1.9l.6-.6 1.6 1-.6 1.2C5.6 8.7 3.3 6.4 3 4z" fill="#0d0d0d"/></svg>
        314 862.4490
      </li>
      <li>
        <svg viewBox="0 0 12 12" aria-hidden="true"><circle cx="6" cy="6" r="6" fill="#fff"/><rect x="3" y="4" width="6" height="4.2" fill="none" stroke="#0d0d0d" stroke-width="0.9"/><path d="M3 4l3 2.3L9 4" fill="none" stroke="#0d0d0d" stroke-width="0.9"/></svg>
        gil@falcrestsecurityservices.example
      </li>
    </ul>
  </section>

  <section class="card card--back" aria-label="Business card back">
    <svg class="card__bands" viewBox="0 0 500 286" aria-hidden="true">
      <defs>
        <linearGradient id="goldBack" x1="1" y1="0" x2="0" y2="1">
          <stop offset="0" stop-color="var(--gold-light)"/>
          <stop offset="0.5" stop-color="var(--gold-mid)"/>
          <stop offset="1" stop-color="var(--gold-deep)"/>
        </linearGradient>
      </defs>
      <rect width="500" height="286" fill="url(#goldBack)"/>
      <polygon fill="var(--ink)"
        points="0,0 500,0 500,84 420,84 420,168 86,168 86,196 0,196"/>
    </svg>
    <div class="wordmark"><span class="wordmark__dot"></span>Falcrest</div>
    <p class="website">www.falcrestsecurityservices.example</p>
  </section>

</main>
</body>
</html>
```